M Zyvantics Buisness Cards

I need a technology focused clean business card for my employees. I have attached out logo to include in the mocks. We're a modern tech consulting firm that drives to interface humanity with technology in a truly cohesive fashion.

```html
<!DOCTYPE html>
<html lang="en">
<head>
<meta charset="utf-8">
<title>M Zyvantics Business Cards</title>
<link href="https://fonts.googleapis.com/css2?family=Lato:wght@300;400;700;900&display=swap" rel="stylesheet">
<style>
  :root {
    --page-bg: #2a2a2a;
    --card-bg: #1c1c1d;
    --card-bg-light: #262627;
    --card-bg-dark: #141415;
    --ink-white: #ffffff;
    --ink-soft: #e6e6e6;
    --accent-blue: #1f86d6;
  }
  * { margin: 0; padding: 0; box-sizing: border-box; }
  html, body {
    width: 1200px; height: 900px; overflow: hidden;
    background: var(--page-bg);
    font-family: "Lato", sans-serif;
  }
  .stage {
    position: relative; width: 1200px; height: 900px;
    display: flex; flex-direction: column; align-items: center; justify-content: center; gap: 44px;
  }
  .card {
    position: relative; width: 560px; height: 320px;
    border-radius: 14px; overflow: hidden;
    background: var(--card-bg);
    box-shadow: 0 10px 30px rgba(0,0,0,0.45);
  }
  /* front */
  .card-front .facet-texture {
    position: absolute; inset: 0;
    background: linear-gradient(135deg, var(--card-bg-light) 0%, var(--card-bg) 45%, var(--card-bg-dark) 100%);
  }
  .brand-lockup {
    position: absolute; left: 0; right: 0; top: 112px;
    display: flex; align-items: center; justify-content: center; gap: 14px;
  }
  .brand-dot {
    width: 52px; height: 52px; border-radius: 50%;
    border: 6px solid var(--ink-white);
  }
  .brand-name {
    color: var(--ink-white); font-weight: 900; font-size: 44px; letter-spacing: 2px;
  }
  .web-address {
    position: absolute; right: 84px; top: 214px;
    color: var(--ink-white); font-weight: 700; font-size: 12px; letter-spacing: 3px;
  }
  /* back */
  .person {
    position: absolute; left: 150px; top: 140px; text-align: right; width: 180px;
  }
  .person-name { color: var(--accent-blue); font-size: 18px; letter-spacing: 0.5px; white-space: nowrap; }
  .person-name .first { font-weight: 300; }
  .person-name .last { font-weight: 900; }
  .person-title { color: var(--ink-white); font-size: 12px; margin-top: 2px; }
  .divider {
    position: absolute; left: 348px; top: 104px; width: 2px; height: 96px;
    background: var(--ink-soft);
  }
  .contact-list {
    position: absolute; left: 372px; top: 108px; list-style: none;
  }
  .contact-list li {
    display: flex; align-items: center; gap: 10px;
    color: var(--ink-white); font-size: 12.5px; height: 22px;
  }
  .contact-list svg { width: 13px; height: 13px; fill: var(--accent-blue); flex: none; }
</style>
</head>
<body>
<main class="stage">
  <section class="card card-front" aria-label="Business card front">
    <div class="facet-texture" role="img" aria-label="Faint dark faceted polygon background texture"></div>
    <div class="brand-lockup">
      <span class="brand-dot"></span>
      <span class="brand-name">M ZYVANTICS</span>
    </div>
    <p class="web-address">www.mzyvantics.com</p>
  </section>

  <section class="card card-back" aria-label="Business card back">
    <div class="person">
      <p class="person-name"><span class="first">ADRIAN </span><span class="last">VELMONT</span></p>
      <p class="person-title">Principal Director</p>
    </div>
    <div class="divider"></div>
    <ul class="contact-list">
      <li>
        <svg viewBox="0 0 16 16" aria-hidden="true"><path d="M1 5c0-2 3-3 7-3s7 1 7 3v1h-4V5H5v1H1z"/><path d="M3 8l2-2h6l2 2v6H3z"/></svg>
        555.304.7121
      </li>
      <li>
        <svg viewBox="0 0 16 16" aria-hidden="true"><path d="M4 1l3 3-2 2c1 2 3 4 5 5l2-2 3 3-2 3C7 15 1 9 1 3z"/></svg>
        555.318.6003
      </li>
      <li>
        <svg viewBox="0 0 16 16" aria-hidden="true"><path d="M4 1h8v4H4z"/><path d="M1 6h14v6h-3v-2H4v2H1z"/><path d="M5 11h6v4H5z"/></svg>
        555.302.8025
      </li>
      <li>
        <svg viewBox="0 0 16 16" aria-hidden="true"><path d="M1 3h14v1L8 9 1 4z"/><path d="M1 6l7 5 7-5v7H1z"/></svg>
        avelmont@mzyvantics.com
      </li>
    </ul>
  </section>
</main>
</body>
</html>
```